Communication and Marketing agency needs a new presentation card

We are a group of communication and marketing agencies specialized in companies that are in the logistics and industrial sector. The head agency is TELVANO Grupo and the group consists of 4 agencies: TELVANO Media, TELVANO Digital, TELVANO Research and EnlazaPorImagen. We hace 4 offices in Spain (Madrid, Barcelona, Valencia and Murcia). We are looking for a clean and attractive design that transmits our experience, brand presence in the market and knowledge to those who receive the card.It has to maintain the colors of the logo that is attached.
Target Market(s)
logistics and industrial sector
Marketing department
Clean and attractive design

```html
<!DOCTYPE html>
<html lang="es">
<head>
<meta charset="utf-8">
<title>TELVANO Grupo – Tarjeta de presentación</title>
<link rel="stylesheet" href="https://fonts.googleapis.com/css2?family=Roboto+Condensed:wght@300;400;700&display=swap">
<style>
  :root {
    --page-bg: #e6e4e1;
    --card-dark-top: #3b3838;
    --card-dark-bottom: #242121;
    --card-light: #ffffff;
    --panel-light: #f1f0ef;
    --ink-white: #ffffff;
    --ink-soft: #cfcbcb;
    --brand-red: #c1272d;
    --brand-grey: #5b5b5b;
  }
  * { box-sizing: border-box; margin: 0; padding: 0; }
  html, body {
    width: 1200px; height: 900px; overflow: hidden;
    background: var(--page-bg);
    font-family: "Roboto Condensed", "Arial Narrow", sans-serif;
  }
  .stage {
    width: 1200px; height: 900px;
    display: flex; align-items: center; justify-content: center; gap: 80px;
  }
  .card {
    position: relative;
    width: 340px; height: 525px;
    box-shadow: 0 14px 30px rgba(0,0,0,.22);
  }
  /* Front */
  .card--front {
    background: linear-gradient(160deg, var(--card-dark-top), var(--card-dark-bottom));
    color: var(--ink-white);
  }
  .holder {
    position: absolute; top: 36px; right: 34px; text-align: right;
  }
  .holder__name { font-size: 27px; font-weight: 400; letter-spacing: .3px; }
  .holder__role { font-size: 17px; font-weight: 300; color: var(--ink-soft); margin-top: 2px; }
  .frame {
    position: absolute; top: 128px; left: 32px; right: 32px; bottom: 32px;
    border: 2px solid var(--ink-white);
  }
  .contact {
    position: absolute; top: 22px; right: 20px; text-align: right;
    list-style: none; font-size: 16px; font-weight: 300; line-height: 1.6;
  }
  .contact__web { font-weight: 400; font-size: 17px; margin-top: 4px; }
  .contact__dot {
    display: inline-block; width: 13px; height: 13px; border-radius: 50%;
    background: var(--ink-white); margin-right: 6px; vertical-align: -1px;
  }
  .wordmark { line-height: 1; }
  .wordmark--front {
    position: absolute; left: 24px; bottom: 26px;
    font-size: 34px; font-weight: 300; letter-spacing: 2px; color: var(--ink-white);
  }
  /* Back */
  .card--back { background: var(--card-light); }
  .agency-panel {
    position: absolute; top: 30px; left: 30px; right: 30px; height: 300px;
    background: var(--panel-light);
    display: flex; flex-direction: column; align-items: flex-end; justify-content: center;
    gap: 22px; padding-right: 26px;
  }
  .agency {
    font-size: 22px; font-weight: 400; color: var(--brand-red); letter-spacing: .5px;
  }
  .wordmark--back {
    position: absolute; left: 34px; bottom: 48px;
    font-size: 50px; font-weight: 400; letter-spacing: 2px; color: var(--brand-red);
  }
</style>
</head>
<body>
<main class="stage">
  <section class="card card--front" aria-label="Cara delantera">
    <header class="holder">
      <p class="holder__name">Alberto Quiroga</p>
      <p class="holder__role">Director</p>
    </header>
    <div class="frame">
      <ul class="contact">
        <li>T. 910 472 318</li>
        <li>M. 641 205 789</li>
        <li>aquiroga@telvano.es</li>
        <li><span class="contact__dot"></span>albertoquiroga</li>
        <li class="contact__web">www.telvano.es</li>
      </ul>
      <p class="wordmark wordmark--front">TELVANO Grupo</p>
    </div>
  </section>

  <section class="card card--back" aria-label="Cara trasera">
    <div class="agency-panel">
      <p class="agency">TELVANO Digital</p>
      <p class="agency">TELVANO Media</p>
      <p class="agency">TELVANO Research</p>
      <p class="agency">EnlazaPorImagen</p>
    </div>
    <p class="wordmark wordmark--back">TELVANO Grupo</p>
  </section>
</main>
</body>
</html>
```